Business Card - Rebranding for Consulting Firm

We are renaming and rebranding our consulting firm and need to raise the level of quality of our cards as part of that effort. We consult to leading high tech, life science and other innovation sector companies.

Need a two-sided business card design.

Side 1: (a) Company logo (b) tag line: Make Every Hire Count for More (c) Name (d) Title (e) Phone 1: Office (f) Phone 2: Mobile (g) email: person@HollowmereAdvisory.com

Side 2: Two lines of text: (a) Markets Shift Fast. Teams Must Adapt. People Carry the Plan Forward. (b) We help you lead on all three.

Target Market(s)

Business and human resources executives and senior managers

Industry/Entity Type

Management Consulting

Contact Information for Business Card

Font styles to use
Sans Serif

Requirements
Must have
• clean, not too busy, but with a bit of creativity. Stick to the colors used in the attached logo
• appeal to high tech, life science companies
Nice to have
• prefer white background

```html
<!DOCTYPE html>
<html lang="en">
<head>
<meta charset="utf-8">
<title>Hollowmere Advisory – Business Card</title>
<link href="https://fonts.googleapis.com/css2?family=Open+Sans:wght@400;600&family=Roboto+Condensed:wght@400;500&display=swap" rel="stylesheet">
<style>
  :root {
    --page-bg: #e6e4e1;
    --card-white: #ffffff;
    --brand-blue: #1a6fa8;
    --brand-blue-deep: #0a6aa6;
    --brand-blue-bright: #00a9de;
    --slate-band: #6f8796;
    --text-grey: #4a4f54;
    --title-grey: #6d7a84;
    --white: #ffffff;
  }
  * { box-sizing: border-box; margin: 0; padding: 0; }
  html, body {
    width: 1200px; height: 987px; overflow: hidden;
    background: var(--page-bg);
  }
  .canvas { position: relative; width: 1200px; height: 987px; }

  .card {
    position: absolute; left: 293px; width: 615px; height: 351px;
    overflow: hidden;
  }

  /* Front side */
  .card-front { top: 130px; background: var(--card-white); }
  .front-brand {
    position: absolute; left: 24px; top: 150px;
    display: flex; align-items: center; gap: 10px;
  }
  .brand-square { width: 16px; height: 16px; background: var(--brand-blue); }
  .brand-name {
    font-family: "Open Sans", sans-serif; font-weight: 600;
    font-size: 23px; color: var(--brand-blue); letter-spacing: -0.2px;
  }
  .contact-block { position: absolute; left: 305px; top: 86px; }
  .person-name {
    font-family: "Open Sans", sans-serif; font-weight: 600;
    font-size: 21px; color: var(--brand-blue); letter-spacing: 0.3px;
  }
  .person-title {
    font-family: "Open Sans", sans-serif; font-size: 16px;
    color: var(--title-grey); margin-bottom: 10px;
  }
  .contact-line {
    display: flex; align-items: center; gap: 9px;
    font-family: "Open Sans", sans-serif; font-size: 16px;
    color: var(--text-grey); height: 24px;
  }
  .contact-line svg { width: 15px; height: 15px; fill: var(--brand-blue); flex: none; }
  .website {
    font-family: "Open Sans", sans-serif; font-weight: 600;
    font-size: 16px; color: var(--brand-blue); margin-top: 10px;
  }
  .tagline-band {
    position: absolute; left: 0; bottom: 0; width: 100%; height: 34px;
    background: var(--slate-band);
    display: flex; align-items: center; justify-content: center;
    font-family: "Roboto Condensed", sans-serif; font-weight: 500;
    font-size: 19px; color: var(--white);
  }

  /* Back side */
  .card-back {
    top: 506px;
    background: radial-gradient(ellipse 60% 75% at 50% 42%, var(--brand-blue-bright) 0%, var(--brand-blue-deep) 100%);
  }
  .back-brand {
    position: absolute; left: 0; top: 142px; width: 100%;
    display: flex; align-items: center; justify-content: center; gap: 14px;
  }
  .back-brand .brand-square { width: 24px; height: 24px; background: var(--white); }
  .back-brand .brand-name { font-size: 40px; color: var(--white); }
  .back-message {
    position: absolute; left: 0; top: 270px; width: 100%; text-align: center;
    font-family: "Roboto Condensed", sans-serif; font-weight: 500;
    font-size: 16px; color: var(--white); text-transform: uppercase;
  }
  .message-rule {
    width: 470px; height: 1px; margin: 8px auto;
    background: rgba(255,255,255,0.45);
  }
</style>
</head>
<body>
<main class="canvas">

  <section class="card card-front" aria-label="Business card front">
    <div class="front-brand">
      <span class="brand-square"></span>
      <span class="brand-name">Hollowmere Advisory</span>
    </div>

    <div class="contact-block">
      <p class="person-name">DANIEL REYES</p>
      <p class="person-title">CEO/Founder</p>
      <p class="contact-line">
        <svg viewBox="0 0 24 24" aria-hidden="true"><path d="M6.6 10.8c1.4 2.8 3.8 5.1 6.6 6.6l2.2-2.2c.3-.3.7-.4 1-.2 1.1.4 2.3.6 3.6.6.6 0 1 .4 1 1V20c0 .6-.4 1-1 1C10.6 21 3 13.4 3 4c0-.6.4-1 1-1h3.5c.6 0 1 .4 1 1 0 1.3.2 2.5.6 3.6.1.3 0 .7-.2 1z"/></svg>
        555 210 4471
      </p>
      <p class="contact-line">
        <svg viewBox="0 0 24 24" aria-hidden="true"><path d="M7 1h10a2 2 0 0 1 2 2v18a2 2 0 0 1-2 2H7a2 2 0 0 1-2-2V3a2 2 0 0 1 2-2zm0 3v14h10V4H7zm5 15.5a1 1 0 1 0 0 2 1 1 0 0 0 0-2z"/></svg>
        555 380 9152
      </p>
      <p class="contact-line">
        <svg viewBox="0 0 24 24" aria-hidden="true"><path d="M2 5h20v14H2V5zm2 2v.5l8 5 8-5V7H4zm0 2.8V17h16V9.8l-8 5-8-5z"/></svg>
        person@HollowmereAdvisory.com
      </p>
      <p class="website">www.HollowmereAdvisory.com</p>
    </div>

    <div class="tagline-band">Make Every Hire Count for More</div>
  </section>

  <section class="card card-back" aria-label="Business card back">
    <div class="back-brand">
      <span class="brand-square"></span>
      <span class="brand-name">Hollowmere Advisory</span>
    </div>
    <div class="back-message">
      <p>Markets shift fast. Teams must adapt. People carry the plan forward.</p>
      <div class="message-rule"></div>
      <p>We help you lead on all three.</p>
    </div>
  </section>

</main>
</body>
</html>
```